Anzeigengestaltung für Stellenanzeige
Zielgruppe
Wir sind ein Abrechnungsunternehmen das für Zahnärzte die zahnmedizinische und zahntechnische Abrechnung von extern übernimmt.
Aufgrund einer Erweiterung suchen wir neues Personal welches uns unterstützt. Deshalb benötigen wir einen Stellenanzeige.
Wir suchen Personal - zahnmedizinische Fachangestellte mit Erfahrung in der Abrechnung
Abkürzungen: ZFA oder ZMV beides gewünscht wenn Abrechnungskenntnisse vorhanden sind.
Aufgabenstellung
Bitte Stellenanzeige unserer Website anpassen, www.zahnkanzleimerwen.de
logo bitte con Website übernehmen.
Moderne Gestaltung
Wir bieten:
-Anstellung Teilzeit oder Vollzeit
-Ein motiviertes und kompetentes Team
-Fort- und Weitermöglichkeiten
-Flexible Arbeits- und Urlaubszeiten
-Attraktive leistungsgerechte Bezahlung
Ihr Profil
Um die Stelle gut ausfüllen zu können, wünschen wir uns von Ihnen:
Abgeschlossene Ausbildung zum/zur Zahnmedizinische Fachangestellte, Zahnmedizinische Verwaltungsfachangestellte (m/w/d)
Selbstständiges Arbeiten und Einsatzbereitschaft
Gute PC-Kenntnisse und sicherer Umgang mit gängigen Office-Anwendungen
Erfahrung in der zahmedizinischen Abrechnung
Sorgfalt, Teamfähigkeit
Engagement und Freude am Beruf
Wir haben Ihr Interesse geweckt dann senden Sie uns Ihre Bewerbung an: t.brellmann@zahnkanzleimerwen.de
------Beispiel----------
Gerne auch eigene Beispiele....

```html
<!DOCTYPE html>
<html lang="de">
<head>
<meta charset="utf-8">
<title>Stellenanzeige – Merwen Dental</title>
<link rel="stylesheet" href="https://fonts.googleapis.com/css2?family=Poppins:wght@300;400;500;600&family=Gochi+Hand&display=swap">
<style>
  :root{
    --page:#151515;
    --flyer:#1f1f1f;
    --flyer-light:#2a2a2a;
    --text:#ecebea;
    --muted:#d9d6d2;
    --brand:#cdc6bd;
    --photo-warm:#8a7a68;
    --photo-light:#d8c8ae;
  }
  *{margin:0;padding:0;box-sizing:border-box}
  html,body{width:1200px;height:2400px;overflow:hidden;background:var(--page)}
  body{font-family:"Poppins",sans-serif;color:var(--text);position:relative}
  .flyer{
    position:absolute;left:40px;top:406px;width:1120px;height:1587px;
    background:radial-gradient(ellipse at 50% 35%,var(--flyer-light) 0%,var(--flyer) 60%,#191919 100%);
    overflow:hidden;
  }
  .team-photo{
    position:absolute;left:60px;top:0;width:1000px;height:560px;
    background:
      radial-gradient(ellipse 26% 50% at 30% 45%,var(--photo-light) 0%,var(--photo-warm) 45%,rgba(60,52,44,0) 100%),
      radial-gradient(ellipse 26% 50% at 72% 52%,#e6dcc8 0%,#9d8d78 45%,rgba(60,52,44,0) 100%),
      linear-gradient(180deg,#1c1c1c 0%,#262422 60%,var(--flyer) 100%);
  }
  .team-photo::after{
    content:"";position:absolute;left:0;right:0;bottom:0;height:140px;
    background:linear-gradient(180deg,rgba(31,31,31,0),var(--flyer));
  }
  .brand-name{
    position:absolute;left:0;right:0;top:496px;text-align:center;
    font-weight:600;font-size:116px;letter-spacing:-4px;line-height:1;color:var(--brand);
  }
  .brand-tagline{
    position:absolute;left:0;right:0;top:622px;text-align:center;
    font-weight:400;font-size:31px;line-height:1.2;letter-spacing:.2em;color:var(--muted);
  }
  .headline{
    position:absolute;left:100px;top:686px;width:400px;
    font-family:"Gochi Hand",cursive;font-weight:400;font-size:52px;line-height:.98;color:#fff;
    transform:rotate(-2deg);transform-origin:left top;
  }
  .headline span{display:block;padding-left:34px}
  .col-title{font-weight:600;font-size:30px;line-height:1.25;color:#fff}
  .offer{position:absolute;left:66px;top:815px;width:440px}
  .profile{position:absolute;left:545px;top:752px;width:500px}
  ul.bullets{list-style:none;margin-top:34px}
  ul.bullets li{
    position:relative;padding-left:30px;margin-bottom:8px;
    font-weight:300;font-size:24px;line-height:1.2;color:var(--muted);
  }
  ul.bullets li::before{content:"•";position:absolute;left:4px;top:0}
  .profile ul.bullets{margin-top:30px}
  .apply{
    position:absolute;left:0;right:0;top:1392px;text-align:center;
    font-weight:300;font-size:25px;line-height:1.3;color:var(--text);
  }
  .apply strong{font-weight:600}
  .contact{
    position:absolute;left:54px;right:40px;top:1500px;
    display:flex;justify-content:space-between;font-weight:300;font-size:21px;line-height:1.3;color:var(--muted);
  }
  .contact-item{display:flex;gap:12px;align-items:flex-start}
  .contact-item .lines div{display:flex;align-items:center;gap:12px;white-space:nowrap}
  .contact-item svg{width:20px;height:20px;flex:none;fill:var(--text)}
  .contact-item .web{font-weight:600;color:#fff}
</style>
</head>
<body>
  <main class="flyer">
    <div class="team-photo" role="img" aria-label="Porträtfoto von zwei lächelnden Mitarbeiterinnen vor dunklem Hintergrund"></div>

    <div class="brand-name">Merwen Dental</div>
    <div class="brand-tagline">Zahnärztliche Abrechnung &amp; Management</div>

    <h1 class="headline">Wir suchen<span>Verstärkung!</span></h1>

    <section class="offer">
      <h2 class="col-title">Wir bieten:</h2>
      <ul class="bullets">
        <li>Anstellung Teilzeit oder Vollzeit</li>
        <li>Ein motiviertes und<br>kompetentes Team</li>
        <li>Fort- und Weiterbildungs-<br>möglichkeiten</li>
        <li>Flexible Arbeits- und<br>Urlaubszeiten</li>
        <li>Attraktive leistungsgerechte<br>Bezahlung</li>
      </ul>
    </section>

    <section class="profile">
      <h2 class="col-title">Um die Stelle gut ausfüllen zu können, wünschen wir uns von Ihnen:</h2>
      <ul class="bullets">
        <li>Abgeschlossene Ausbildung zum/<br>zur Zahnmedizinische<br>Fachangestellten, Zahnmedizini-<br>sche Verwaltungsfachangestellte<br>(m/w/d)</li>
        <li>Selbstständiges Arbeiten und<br>Einsatzbereitschaft</li>
        <li>Gute PC-Kenntnisse und<br>sicherer Umgang<br>mit den gängigen Office-<br>Anwendungen</li>
        <li>Erfahrung in der zahmedizinischen<br>Abrechnung</li>
        <li>Sorgfalt, Teamfähigkeit</li>
        <li>Engagement und Freude am Beruf</li>
      </ul>
    </section>

    <p class="apply">Wir haben Ihr Interesse geweckt? Dann senden Sie uns Ihre<br>vollständige&nbsp; Bewerbung an: <strong>t.brellmann@zahnkanzleimerwen.de</strong></p>

    <footer class="contact">
      <div class="contact-item">
        <svg viewBox="0 0 24 24"><path d="M12 2a7 7 0 0 0-7 7c0 5 7 13 7 13s7-8 7-13a7 7 0 0 0-7-7zm0 3.5a3.5 3.5 0 1 1 0 7 3.5 3.5 0 0 1 0-7z"/></svg>
        <div class="lines"><div>Lindenweg 12, 67433 Rheinau</div><div>Mühlgasse 5, 67435 Talheim</div></div>
      </div>
      <div class="contact-item">
        <div class="lines">
          <div><svg viewBox="0 0 24 24"><path d="M6.6 10.8a15 15 0 0 0 6.6 6.6l2.2-2.2a1 1 0 0 1 1-.25 11.4 11.4 0 0 0 3.6.57 1 1 0 0 1 1 1V20a1 1 0 0 1-1 1A17 17 0 0 1 3 4a1 1 0 0 1 1-1h3.5a1 1 0 0 1 1 1c0 1.25.2 2.45.57 3.57a1 1 0 0 1-.25 1z"/></svg>06000 - 12 34 567</div>
          <div><svg viewBox="0 0 24 24"><path d="M6 2h8l5 5v15H6zm2 2v16h9V8h-4V4z"/></svg>06000 - 12 34 589</div>
        </div>
      </div>
      <div class="contact-item">
        <div class="lines">
          <div><svg viewBox="0 0 24 24"><path d="M3 5h18v14H3zm2 2v.5l7 4.5 7-4.5V7zm0 2.9V17h14V9.9l-7 4.5z"/></svg>info@zahnkanzleimerwen.de</div>
          <div class="web"><svg viewBox="0 0 24 24"><path d="M5 3l14 7-6 1.8 4 6.7-2.6 1.5-4-6.7L6 17z"/></svg>www.zahnkanzleimerwen.de</div>
        </div>
      </div>
    </footer>
  </main>
</body>
</html>
```